Healthy Food Healthy Brain Rack Card

We want a new 2 page (front and page) 3.67" x 8.5" rack card. This rack card is the first of a series we are creating. We will have five more eventually.

The minimum font size for the text on the front is 11 point and also for other main body text.

Use the text on the word document.

The images and layout in the word document are just sample ideas we had.

We have a subscripton to adobe stock images so prefer to get images from there or free high quality images.

The document is for older readers. Do not put text over graphics and keep it simple and easy to read with high contrast.

We are open to any color scheme, though something that conveys fresh and healthy, is good.

We want some very simple design element(s) incorporated that convey Native American communities or heritage. But NO head dress, teepee graphics, etc.

At the top, of the first page we would like a collage of healthy food images. This can include fish, chicken, fresh vegetables, berries, brown rice, etc.

On the back side, the text below the brown box on the word document with the title "mock up" can be smaller as needed.

Please remember to include the funding statement - it can be in a very small font 6/7 point.

For more information about our project, please visit https://velmorcollective.org/mind-care/

```html
<!DOCTYPE html>
<html lang="en">
<head>
<meta charset="utf-8">
<title>Healthy Food, Healthy Brain – Rack Card</title>
<link href="https://fonts.googleapis.com/css2?family=Open+Sans:wght@400;600;700&family=PT+Sans+Narrow:wght@400;700&display=swap" rel="stylesheet">
<style>
  :root{
    --teal:#4a9ca6;
    --teal-dark:#3f8a93;
    --rust:#a9544b;
    --ink:#2b2b2b;
    --paper:#ffffff;
    --bg:#e4e4e4;
    --mist:#eeeeee;
  }
  *{box-sizing:border-box;margin:0;padding:0}
  html,body{width:682px;height:1200px;overflow:hidden;background:var(--bg)}
  body{font-family:"PT Sans Narrow",sans-serif;color:var(--ink);position:relative}
  .card{position:absolute;top:247px;width:305px;height:706px;background:var(--paper);overflow:hidden;box-shadow:0 3px 8px rgba(0,0,0,.25)}
  .card--front{left:24px}
  .card--back{left:353px}

  .photo{display:block;width:100%}
  .photo--top{height:104px;background:linear-gradient(120deg,#2e3a3f 0%,#6b4a35 30%,#c9a06a 55%,#5f7d3a 75%,#2c3438 100%)}
  .photo--bottom{position:absolute;left:0;bottom:0;height:62px;background:linear-gradient(90deg,#5a3a2e,#d8633f 25%,#6a4233 50%,#d56a48 75%,#5a3a2e)}
  .band{display:block;width:100%;height:14px;background:linear-gradient(90deg,#b77a72,#8fb8bd 50%,#b77a72)}

  .front-body{padding:8px 26px 0 26px}
  .title{font-family:"Open Sans",sans-serif;font-weight:700;font-size:15.5px;letter-spacing:.1px;color:var(--teal);padding-bottom:3px;border-bottom:1px solid var(--teal);white-space:nowrap}
  .title .accent{color:var(--rust)}
  .intro{font-size:11px;line-height:15px;margin-top:8px}

  .steps{position:relative;margin-top:12px;padding-bottom:16px}
  .steps-tab{position:relative;z-index:1;display:inline-block;background:var(--teal);color:#fff;font-family:"Open Sans",sans-serif;font-weight:600;font-size:10.5px;line-height:14px;padding:3px 6px;border-radius:4px 0 0 4px;white-space:nowrap}
  .steps-frame{position:absolute;left:8px;right:0;top:10px;bottom:6px;border:1.5px solid var(--teal);border-left:none;border-radius:0 6px 6px 0;pointer-events:none;z-index:0}
  .steps-frame::before{content:"";position:absolute;left:-4px;bottom:-4.5px;width:7px;height:7px;border-radius:50%;background:var(--teal)}
  .steps-list{position:relative;z-index:1;list-style:none;margin:8px 20px 0 0}
  .steps-list li{position:relative;padding-left:18px;font-size:10.5px;line-height:14px;margin-bottom:6px}
  .steps-list li::before{content:"";position:absolute;left:1px;top:4px;width:6px;height:6px;border-radius:50%;background:#7d8a8c}

  .note{font-size:10.5px;margin-top:10px}
  .doctor{font-family:"Open Sans",sans-serif;font-weight:700;font-size:11px;line-height:14px;color:var(--rust);margin-top:9px}
  .quote{position:relative;margin-top:14px;padding-left:12px;font-family:"Open Sans",sans-serif;font-size:10.5px;line-height:14.5px}
  .quote .mark{font-weight:700;color:var(--teal);font-size:16px;line-height:1}
  .quote .mark--open{position:absolute;left:0;top:-8px}
  .quote .mark--close{display:inline-block;vertical-align:-8px;margin-left:4px}
  .quote cite{display:block;font-style:normal;margin-top:2px}
  .quote cite strong{font-weight:700}
  .front-footer{position:absolute;left:0;right:0;bottom:62px}

  .back-title{font-family:"Open Sans",sans-serif;font-weight:700;font-size:18px;text-align:center;color:var(--teal);margin-top:8px;letter-spacing:.2px}
  .back-title span{color:var(--rust);border-bottom:1px solid var(--rust)}
  .back-title .u{border-bottom:1px solid var(--teal)}
  .recipe-name{font-family:"Open Sans",sans-serif;font-weight:700;font-size:11px;color:var(--rust);margin:6px 0 0 26px;display:inline-block;border-bottom:1px solid var(--rust);padding-bottom:1px}
  .recipe-top{display:flex;gap:8px;margin:8px 14px 0 14px;padding:2px 0 10px 13px;background:linear-gradient(90deg,#fff 30%,var(--mist))}
  .recipe-photo{width:118px;height:169px;border:1.5px solid var(--rust);padding:5px;flex:none}
  .recipe-photo .fill{width:100%;height:100%;background:linear-gradient(135deg,#dfe3e8,#c6d8a8 35%,#ef8f6e 60%,#d8dde2)}
  .ingredients h3{font-family:"Open Sans",sans-serif;font-weight:600;font-size:11px;margin-bottom:4px}
  .ingredients ul{list-style:none}
  .ingredients li{position:relative;padding-left:12px;font-size:10.5px;line-height:15.3px}
  .ingredients li::before{content:"";position:absolute;left:0;top:5px;width:5px;height:5px;border-radius:50%;background:#7d8a8c}
  .ingredients li.sub::before{display:none}

  .method{list-style:none;margin:6px 22px 0 26px}
  .method li{position:relative;padding-left:14px;font-size:10.5px;line-height:14.5px;margin-bottom:6px}
  .method li::before{content:"";position:absolute;left:0;top:3px;border-left:7px solid var(--teal);border-top:4.5px solid transparent;border-bottom:4.5px solid transparent}
  .method li:nth-child(even)::before{border-left-color:var(--rust)}

  .callout{background:var(--teal);color:#fff;font-weight:700;font-size:11px;line-height:14.5px;padding:6px 26px 7px 26px;margin-top:4px}
  .info{padding:8px 26px 0 26px}
  .info h3{display:flex;align-items:center;gap:6px;font-family:"Open Sans",sans-serif;font-weight:600;font-size:11px;color:var(--rust)}
  .info h3::after{content:"";flex:1;height:1px;background:#222}
  .info p{font-size:8px;line-height:12px;margin-top:3px}
  .info .lk-teal{color:var(--teal);font-weight:700}
  .info .lk-rust{color:var(--rust);font-weight:700}
  .org{display:flex;align-items:center;justify-content:flex-end;gap:5px;margin-top:-8px}
  .org-dot{width:24px;height:24px;border-radius:50%;background:var(--teal)}
  .org-name{font-weight:700;font-size:10px;color:var(--teal)}
  .funding{font-weight:700;font-size:5.5px;line-height:7.5px;padding:8px 26px 0 26px}
  .back-footer{position:absolute;left:0;right:0;bottom:0}
</style>
</head>
<body>

<section class="card card--front" aria-label="Rack card front">
  <div class="photo photo--top" role="img" aria-label="Collage of healthy foods: grilled chicken, vegetables, rice, olives and fruit"></div>
  <div class="band" role="img" aria-label="Teal and rust chevron border"></div>
  <div class="front-body">
    <h1 class="title">HEALTHY FOOD, <span class="accent">HEALTHY BRAIN</span></h1>
    <p class="intro">Everyone slows down as they get older, both in body and mind. Eating healthier food can help your overall health, including brain health. It may also reduce your risk for memory loss and problems thinking.</p>
    <div class="steps">
      <div class="steps-frame"></div>
      <span class="steps-tab">Healthier steps to protect your brain:</span>
      <ul class="steps-list">
        <li>Eat more vegetables, fruits, whole grains, and lower-fat milk.</li>
        <li>Use less salt and added sugar.</li>
        <li>Eat more fish, chicken, turkey, beans, and nuts.</li>
        <li>Cut down on bad fats (“saturated” and trans), cholesterol, and red meat.</li>
        <li>Buy fresh, not packaged food when you can.</li>
        <li>Limit how much alcohol you drink.</li>
        <li>Learn your daily calorie needs for your body size.</li>
        <li>Take care of your mental and spiritual health to support your physical and brain health.</li>
      </ul>
    </div>
    <p class="note">Small changes can make a big difference for better brain health.</p>
    <p class="doctor">Talk to your doctor about more steps to healthier food choices.</p>
    <blockquote class="quote">
      <span class="mark mark--open">“</span>
      Without the elk, salmon, huckleberries, shellfish, and cedar trees we are nobody…<span class="mark mark--close">”</span>
      <cite><strong>Marla Tenney</strong> (Kessawa)</cite>
    </blockquote>
  </div>
  <div class="front-footer"><div class="band" role="img" aria-label="Teal and rust chevron border"></div></div>
  <div class="photo photo--bottom" role="img" aria-label="Jars of preserved salmon"></div>
</section>

<section class="card card--back" aria-label="Rack card back">
  <div class="band" role="img" aria-label="Teal and rust chevron border"></div>
  <h2 class="back-title"><span class="u" style="color:var(--teal)">MAKE THIS AT</span> <span>HOME</span></h2>
  <div class="recipe-name">GRILLED SALMON &amp; VEGGIE FOIL PACKETS</div>
  <div class="recipe-top">
    <div class="recipe-photo"><div class="fill" role="img" aria-label="Salmon fillet with asparagus, peppers and lemon in foil"></div></div>
    <div class="ingredients">
      <h3>Ingredients -</h3>
      <ul>
        <li>Salmon</li>
        <li>Asparagus</li>
        <li>Red or Green Peppers</li>
        <li class="sub">(Or any seasonal vegetable)</li>
        <li>Onion</li>
        <li>Lemon – sliced</li>
        <li>Basil</li>
        <li>Olive Oil</li>
        <li>Salt and Pepper</li>
        <li>Garlic Powder</li>
      </ul>
    </div>
  </div>
  <ul class="method">
    <li>Cut asparagus, peppers, and onion into bite-size pieces.</li>
    <li>Cut salmon into 4-6 oz pieces.</li>
    <li>Tear tin foil large enough to wrap around salmon &amp; veggies (2 layers).</li>
    <li>Add veggies and salmon to foil.</li>
    <li>Drizzle with olive oil, season with salt, pepper, basil, garlic &amp; top with a piece of sliced lemon.</li>
    <li>Wrap foil tightly around food.</li>
    <li>Grill at 400 degrees for about 20 minutes.<br>Careful opening!</li>
  </ul>
  <p class="callout">Food &amp; drink are a source of strength and connection to community. A return to traditional food pathways and eating local, seasonal fresh foods make healthier eating easier.</p>
  <div class="info">
    <h3>FOR MORE INFORMATION</h3>
    <p>About Healthier Eating - <span class="lk-teal">PlateWise</span> - https://www.platewise.org<br>
    About Brain Health - <span class="lk-rust">Northern Circle Brain Health Center</span> - https://www.northerncirclebrain.org<br>
    <span class="lk-teal">Regional Memory Health Program</span> -<br>https://www.memoryhealthprogram.org</p>
    <div class="org"><span class="org-dot"></span><span class="org-name">NORTHERN CIRCLE</span></div>
  </div>
  <p class="funding">This product is supported by the Regional Health Agency (RHA) of the Department of Community Wellness (DCW) as part of a financial assistance award totaling $348,711 with 100 percent funded by RHA/DCW. The contents are those of the author(s) and do not necessarily represent the official views of, nor an endorsement, by RHA/DCW, or the Government.</p>
  <div class="back-footer"><div class="band" role="img" aria-label="Teal and rust chevron border"></div></div>
</section>

</body>
</html>
```